Thrive Hollow Wording For Logo & Business card

I have the logo, I just need the "thrive Hollow" wording to go with it, and a business card design. The only thing on the business card is the website info. We provide nature connection experiences, and bolster these efforts through writing and host a platform for community around it.

I also have an idea of what it could look like (sketch), though I'm really not sure how it would come out. I am open to the best design and happy to consider original artwork. You can see what the site is about at ThriveHollow.com.

Contact Information for Business Card

The only thing on the business card is the website info and the design. I will put other messaging on the back.

Website lettering (ThriveHollow.com) in Montserrat

Logo Text

Thrive Hollow (letters optional)

Font styles to use
Other font styles liked:
• montserrat

```html
<!DOCTYPE html>
<html lang="en">
<head>
<meta charset="utf-8">
<title>Thrive Hollow – Business Card</title>
<link href="https://fonts.googleapis.com/css2?family=Montserrat:wght@400;500;700;800&display=swap" rel="stylesheet">
<style>
  :root{
    --backdrop:#9a9a9a;
    --paper:#f6f6f4;
    --plum:#3a1d4f;
    --plum-deep:#2c1640;
    --plum-dark:#22102f;
    --plum-light:#4a2d5e;
    --ember:#e8590c;
    --ink-grey:#6d6a70;
    --white:#ffffff;
  }
  *{margin:0;padding:0;box-sizing:border-box}
  html,body{width:1200px;height:801px;overflow:hidden}
  body{
    background:var(--backdrop);
    font-family:"Montserrat",sans-serif;
    display:flex;align-items:center;justify-content:center;gap:48px;
  }
  .card{
    width:540px;height:309px;position:relative;border-radius:4px;
    box-shadow:0 14px 30px rgba(0,0,0,.28);
    overflow:hidden;
  }
  .brand{display:flex;align-items:center;gap:14px}
  .brand__dot{border-radius:50%;flex:none}
  .brand__name{font-weight:800;line-height:1.05;letter-spacing:1px;text-transform:uppercase;white-space:nowrap}

  /* front */
  .card--front{background:var(--paper)}
  .card--front .brand{position:absolute;top:48px;right:44px}
  .card--front .brand__dot{width:64px;height:64px;background:var(--plum-deep)}
  .card--front .brand__name{font-size:24px;color:var(--plum)}
  .divider{position:absolute;left:40px;right:40px;top:170px;height:1px;background:var(--ember)}
  .website{position:absolute;left:40px;top:200px;display:flex;align-items:center;gap:10px;font-size:15px;font-weight:500;color:var(--ink-grey)}
  .website svg{width:13px;height:13px;flex:none}

  /* back */
  .card--back{background:linear-gradient(135deg,var(--plum-deep),var(--plum) 70%,var(--plum-light));display:flex;align-items:center;justify-content:center}
  .card--back .brand{gap:24px}
  .card--back .brand__dot{width:110px;height:110px;background:var(--plum-dark)}
  .card--back .brand__name{font-size:38px;color:var(--white)}
</style>
</head>
<body>
  <section class="card card--front">
    <div class="brand">
      <span class="brand__dot"></span>
      <span class="brand__name">Thrive<br>Hollow</span>
    </div>
    <div class="divider"></div>
    <p class="website">
      <svg viewBox="0 0 24 24" aria-hidden="true" fill="none" stroke="#e8590c" stroke-width="2.2"><circle cx="12" cy="12" r="10"/><path d="M2 12h20M12 2c3 3 3 17 0 20M12 2c-3 3-3 17 0 20"/></svg>
      ThriveHollow.com
    </p>
  </section>

  <section class="card card--back">
    <div class="brand">
      <span class="brand__dot"></span>
      <span class="brand__name">Thrive<br>Hollow</span>
    </div>
  </section>
</body>
</html>
```